KVLO EXTRA PowerPoint

I need to convert our online business to a power point. A step by step presentation,
I want a POWER POINT to use one on one and as well as for a group.
Like to see moving parts to show value and savings. Very clear " dream Vacation" pictures. This is the future of vacationing!

web site:
KVLO.online

two videos below to be included
Updates

The first four days i never received anything. Their was a mixup regarding my power point.

Target Market(s)

dream vacations, for everyone

Number of Pages Required

5+ page

Font styles to use
Sans Serif

Colors

Designer to choose colors to be used in the design.

Requirements
Must have
• Look professional
• movement
Nice to have
• Easy to understand and use. show savings and value
• 10 to 20 pages min.
Should not have
• look nothing like my old power point

```html
<!DOCTYPE html>
<html lang="en">
<head>
<meta charset="utf-8">
<title>KVLO EXTRA – Presentation Slides</title>
<link rel="stylesheet" href="https://fonts.googleapis.com/css2?family=Montserrat:wght@300;400;600;700&display=swap">
<style>
:root{
  --yellow:#f6b800;
  --green:#7ac943;
  --blue:#1ea7e8;
  --dark:#2b2b2b;
  --ink:#333;
  --muted:#8a8a8a;
  --paper:#fff;
  --canvas:#f4f4f4;
  --soft:#efefef;
  --sea:linear-gradient(180deg,#8fd3ee 0%,#2aa3cf 55%,#0f7ea7 100%);
  --beach:linear-gradient(160deg,#f2b35c 0%,#e98d45 30%,#32b6c4 62%,#68c34e 100%);
  --room:linear-gradient(160deg,#c9b39a 0%,#efe6da 50%,#b08a66 100%);
  --forest:linear-gradient(160deg,#1f3d23 0%,#3f6b35 50%,#1a2a1d 100%);
  --meadow:linear-gradient(180deg,#d6e7ef 0%,#a8c99a 55%,#5c8a3c 100%);
}
*{box-sizing:border-box;margin:0;padding:0}
html,body{width:1200px;height:1200px;overflow:hidden}
body{background:var(--canvas);font-family:"Montserrat",sans-serif;color:var(--ink);position:relative}
.slide{position:absolute;width:288px;height:162px;background:var(--paper);overflow:hidden;box-shadow:0 1px 3px rgba(0,0,0,.22)}
.slide.grey{background:var(--soft)}
.a{position:absolute}
.photo{position:absolute}
.sea{background:var(--sea)}
.beach{background:var(--beach)}
.room{background:var(--room)}
.forest{background:var(--forest)}
.meadow{background:var(--meadow)}
.brand{position:absolute;right:6px;bottom:4px;font-size:5.5px;font-weight:700;color:var(--blue);display:flex;align-items:center;gap:2px}
.brand::before{content:"";width:4px;height:4px;border-radius:50%;background:var(--yellow)}
.brand.tl{left:8px;top:6px;right:auto;bottom:auto;color:#fff}
.title{font-weight:300;font-size:9px;line-height:1.2;color:var(--ink)}
.title b{font-weight:700}
.center{text-align:center;left:0;right:0}
.white{color:#fff}
.tx{font-size:3.4px;line-height:1.45;color:var(--muted)}
.tx.w{color:#eee}
.lab{font-size:4px;font-weight:700;color:var(--ink)}
.lab.y{color:var(--yellow)}
.lab.b{color:var(--blue)}
.ic{width:9px;height:9px;fill:currentColor}
.ic.y{color:var(--yellow)}.ic.g{color:var(--green)}.ic.b{color:var(--blue)}
.rule{height:1.5px;width:20px;background:var(--blue)}
.card{position:absolute;background:#fff;box-shadow:0 1px 3px rgba(0,0,0,.2)}
.band{font-size:3.6px;font-weight:700;color:#fff;text-align:center;padding:2px 0}
.bg-y{background:var(--yellow)}.bg-g{background:var(--green)}.bg-b{background:var(--blue)}.bg-k{background:#999}
.price-card{text-align:center}
.price-card .nm{font-size:5.5px;font-weight:300;margin:2px 0 3px}
.price-card ul{list-style:none;text-align:left;padding:4px 6px}
.price-card li{font-size:3.2px;color:var(--muted);line-height:1.7}
.price-card li::before{content:"- "}
.btn{position:absolute;font-size:3.6px;font-weight:700;color:#fff;padding:2.5px 6px}
.strip{position:absolute;display:flex;background:#fff;height:17px}
.strip div{flex:1;display:flex;flex-direction:column;align-items:center;justify-content:center;font-size:2.6px;color:var(--muted)}
.strip div:first-child{color:#fff}
.tile-lab{position:absolute;left:0;right:0;top:18px;text-align:center;font-size:11px;font-weight:600;color:#fff}
.logo-tile{position:absolute;width:40px;height:33px;background:#fff;border:.5px solid #e2e2e2;display:flex;align-items:center;justify-content:center}
.logo-tile span{display:block;width:24px;height:6px;border-radius:2px}
.stars{font-size:6px;color:var(--yellow);letter-spacing:1px}
</style>
</head>
<body>
<svg width="0" height="0" style="position:absolute">
  <symbol id="i-plane" viewBox="0 0 24 24"><path d="M21 16v-2l-8-5V3.5a1.5 1.5 0 0 0-3 0V9l-8 5v2l8-2.5V19l-2 1.5V22l3.5-1 3.5 1v-1.5L13 19v-5.5z"/></symbol>
  <symbol id="i-globe" viewBox="0 0 24 24"><path d="M12 2a10 10 0 1 0 0 20 10 10 0 0 0 0-20zm0 2c1.2 0 2.6 2.6 3 7H9c.4-4.4 1.8-7 3-7zM4.1 11a8 8 0 0 1 3.5-5.8C7.2 6.8 7 8.8 7 11zm0 2H7c0 2.2.2 4.2.6 5.8A8 8 0 0 1 4.1 13zM12 20c-1.2 0-2.6-2.6-3-7h6c-.4 4.4-1.8 7-3 7zm4.4-1.2c.4-1.6.6-3.6.6-5.8h2.9a8 8 0 0 1-3.5 5.8zM17 11c0-2.2-.2-4.2-.6-5.8a8 8 0 0 1 3.5 5.8z"/></symbol>
  <symbol id="i-sun" viewBox="0 0 24 24"><circle cx="12" cy="12" r="5"/><path d="M11 1h2v4h-2zm0 18h2v4h-2zM1 11h4v2H1zm18 0h4v2h-4zM4.2 5.6l1.4-1.4 2.8 2.8-1.4 1.4zm11.4 11.4 1.4-1.4 2.8 2.8-1.4 1.4zM4.2 18.4l2.8-2.8 1.4 1.4-2.8 2.8zM15.6 7l2.8-2.8 1.4 1.4-2.8 2.8z"/></symbol>
  <symbol id="i-mount" viewBox="0 0 24 24"><path d="M2 21 10 5l4 8 2-3 6 11z"/></symbol>
  <symbol id="i-people" viewBox="0 0 24 24"><circle cx="6" cy="5" r="2.5"/><circle cx="12" cy="5" r="2.5"/><circle cx="18" cy="5" r="2.5"/><path d="M3.5 9h5v13h-5zm6 0h5v13h-5zm6 0h5v13h-5z"/></symbol>
  <symbol id="i-hotel" viewBox="0 0 24 24"><path d="M3 4h12v18H3zm2 2v2h3V6zm5 0v2h3V6zM5 10v2h3v-2zm5 0v2h3v-2zM5 14v2h3v-2zm5 0v2h3v-2z"/><path d="m19 2 1 2.5h2.5l-2 1.5.8 2.5L19 7l-2.3 1.5.8-2.5-2-1.5H18z"/></symbol>
  <symbol id="i-bed" viewBox="0 0 24 24"><path d="M2 8h2v6h18v6h-2v-3H4v3H2zm4 1h5v4H6zm7 0h7a2 2 0 0 1 2 2v2h-9z"/></symbol>
  <symbol id="i-pin" viewBox="0 0 24 24"><path d="M12 2a7 7 0 0 0-7 7c0 5 7 13 7 13s7-8 7-13a7 7 0 0 0-7-7zm0 9.5A2.5 2.5 0 1 1 12 6.5a2.5 2.5 0 0 1 0 5z"/></symbol>
  <symbol id="i-car" viewBox="0 0 24 24"><path d="M5 11 7 6h10l2 5h2v6h-2a2 2 0 0 1-4 0H9a2 2 0 0 1-4 0H3v-6z"/></symbol>
  <symbol id="i-sail" viewBox="0 0 24 24"><path d="M12 2v15H4zm2 3 7 12h-7zM2 19h20l-3 3H5z"/></symbol>
  <symbol id="i-cal" viewBox="0 0 24 24"><path d="M3 5h18v17H3zm2 5v10h14V10zM7 2h2v4H7zm8 0h2v4h-2z"/></symbol>
  <symbol id="i-wifi" viewBox="0 0 24 24"><path d="M12 18a2 2 0 1 1 0 4 2 2 0 0 1 0-4zM2 9a15 15 0 0 1 20 0l-2 2a12 12 0 0 0-16 0zm4 4a9 9 0 0 1 12 0l-2 2a6 6 0 0 0-8 0z"/></symbol>
</svg>

<!-- Row 1 -->
<section class="slide" style="left:11px;top:8px">
  <div class="photo sea" style="inset:0" role="img" aria-label="Traveller couple sitting on a seaside harbour wall"></div>
  <div class="brand tl">KVLO</div>
  <div class="a" style="left:24px;top:78px;font-size:21px;font-weight:600;color:#fff">It's Never</div>
  <div class="a" style="left:24px;top:105px;font-size:10px;color:var(--yellow)">Too Late</div>
  <div class="a" style="left:24px;top:120px;width:18px;height:1.5px;background:var(--dark)"></div>
</section>

<section class="slide" style="left:308px;top:8px">
  <div class="photo beach" style="left:155px;top:0;right:0;bottom:0" role="img" aria-label="Beach umbrellas and loungers beside a pool at sunset"></div>
  <div class="a title" style="left:22px;top:28px">KVLO <b>EXTRA</b></div>
  <svg class="ic y a" style="left:22px;top:62px"><use href="#i-plane"/></svg>
  <div class="a" style="left:44px;top:62px;width:100px"><div class="lab">Flight Schedule</div><div class="tx">Book your flight, hotel, excursions and more all in one place.</div></div>
  <svg class="ic g a" style="left:22px;top:90px"><use href="#i-bed"/></svg>
  <div class="a" style="left:44px;top:90px;width:100px"><div class="lab">Selected location</div><div class="tx">Book your flight, hotel, excursions and more all in one place.</div></div>
  <svg class="ic b a" style="left:22px;top:118px"><use href="#i-globe"/></svg>
  <div class="a" style="left:44px;top:118px;width:100px"><div class="lab">World wide</div><div class="tx">Book your flight, hotel, excursions and more all in one place.</div></div>
  <div class="brand" style="left:6px;right:auto">KVLO</div>
</section>

<section class="slide grey" style="left:605px;top:8px">
  <div class="a title center" style="top:20px;font-size:10px">KVLO <b>EXTRA</b></div>
  <svg class="ic y a" style="left:28px;top:62px"><use href="#i-plane"/></svg>
  <div class="a" style="left:50px;top:62px;width:80px"><div class="lab">Flight</div><div class="tx">Book your flight, hotel, excursions and more all in one place.</div></div>
  <svg class="ic g a" style="left:28px;top:90px"><use href="#i-bed"/></svg>
  <div class="a" style="left:50px;top:90px;width:80px"><div class="lab">Summer trip</div><div class="tx">Book your flight, hotel, excursions and more all in one place.</div></div>
  <svg class="ic b a" style="left:28px;top:118px"><use href="#i-globe"/></svg>
  <div class="a" style="left:50px;top:118px;width:80px"><div class="lab">World wide</div><div class="tx">Book your flight, hotel, excursions and more all in one place.</div></div>
  <svg class="ic b a" style="left:156px;top:62px"><use href="#i-sun"/></svg>
  <div class="a" style="left:178px;top:62px;width:80px"><div class="lab">Winter trip</div><div class="tx">Book your flight, hotel, excursions and more all in one place.</div></div>
  <svg class="ic g a" style="left:156px;top:90px"><use href="#i-mount"/></svg>
  <div class="a" style="left:178px;top:90px;width:80px"><div class="lab">Offroad</div><div class="tx">Book your flight, hotel, excursions and more all in one place.</div></div>
  <svg class="ic y a" style="left:156px;top:118px"><use href="#i-mount"/></svg>
  <div class="a" style="left:178px;top:118px;width:80px"><div class="lab">Mountaineer</div><div class="tx">Book your flight, hotel, excursions and more all in one place.</div></div>
</section>

<section class="slide" style="left:902px;top:8px">
  <div class="photo beach" style="left:175px;top:0;right:0;bottom:0" role="img" aria-label="Striped lounge chair on a tropical beach"></div>
  <div class="a" style="left:20px;top:26px;font-size:13px;font-weight:400">Let's get lost!</div>
  <div class="a" style="left:20px;top:44px;font-size:7px;font-weight:300;line-height:1.3">We'll handle the details<br>accurately</div>
  <svg class="ic y a" style="left:24px;top:80px"><use href="#i-plane"/></svg>
  <div class="a" style="left:24px;top:93px;width:50px"><div class="lab y">FLIGHT</div><div class="tx">Book your flight, hotel, excursions and more all in one place.</div></div>
  <svg class="ic g a" style="left:90px;top:80px"><use href="#i-sun"/></svg>
  <div class="a" style="left:90px;top:93px;width:50px"><div class="lab" style="color:var(--green)">SAIL SCHEDULE</div><div class="tx">Book your flight, hotel, excursions and more all in one place.</div></div>
  <div class="brand" style="left:6px;right:auto">KVLO</div>
</section>

<!-- Row 2 -->
<section class="slide" style="left:11px;top:178px">
  <div class="a title" style="left:30px;top:46px;font-size:10px">KVLO <b>EXTRA</b></div>
  <div class="a tx" style="left:30px;top:84px;width:95px">Trip planning today can be challenging. With hundreds of websites, discount sites and hotels it can seem overwhelming.</div>
  <div class="logo-tile" style="left:140px;top:36px"><span style="background:#d8262e"></span></div>
  <div class="logo-tile" style="left:183px;top:36px"><span style="background:#1d3b8a"></span></div>
  <div class="logo-tile" style="left:226px;top:36px"><span style="background:#12365f"></span></div>
  <div class="logo-tile" style="left:140px;top:72px"><span style="background:#c9252c"></span></div>
  <div class="logo-tile" style="left:183px;top:72px"><span style="background:#1c2a6e"></span></div>
  <div class="logo-tile" style="left:226px;top:72px"><span style="background:#b8233a"></span></div>
  <div class="logo-tile" style="left:140px;top:108px"><span style="background:#2a4c9a"></span></div>
  <div class="logo-tile" style="left:183px;top:108px"><span style="background:#1b3e8c"></span></div>
  <div class="logo-tile" style="left:226px;top:108px"><span style="background:#c0195c"></span></div>
  <div class="brand">KVLO</div>
</section>

<section class="slide" style="left:308px;top:178px">
  <div class="a title" style="left:28px;top:24px;font-size:9.5px">Exclusive<br>Travel Rewards<br>For You</div>
  <div class="a tx" style="left:28px;top:72px;width:110px;text-align:justify">Trip planning today can be challenging. With hundreds of websites, discount sites, hotels and accommodations it can seem overwhelming. This network is the exclusive service, offering premium travel opportunities at discount rates. Book your flight, hotel, excursions and more all in one place.</div>
  <div class="a" style="left:160px;top:28px;width:106px;height:106px;border-radius:50%;border:.5px solid #ddd"></div>
  <div class="photo room" style="left:171px;top:39px;width:84px;height:84px;border-radius:50%" role="img" aria-label="Bright hotel bedroom with a large bed"></div>
  <svg class="ic y a" style="left:150px;top:55px"><use href="#i-plane"/></svg>
  <svg class="ic b a" style="left:246px;top:30px"><use href="#i-globe"/></svg>
  <div class="a" style="left:178px;top:22px;width:5px;height:5px;border-radius:50%;background:var(--green)"></div>
  <div class="a" style="left:249px;top:118px;width:5px;height:5px;border-radius:50%;background:var(--yellow)"></div>
  <div class="brand" style="left:6px;right:auto">KVLO</div>
</section>

<section class="slide grey" style="left:605px;top:178px">
  <div class="a title center" style="top:16px;font-size:10px">Check our rate &amp; packages</div>
  <div class="card price-card" style="left:22px;top:44px;width:76px;height:100px"><svg class="ic a" style="position:static;margin-top:6px;color:#555"><use href="#i-plane"/></svg><div class="nm">Silver Trip</div><div class="band bg-g">$1920</div><ul><li>Best services</li><li>Trusted since 1990</li><li>Low prices</li><li>Free booking fee</li></ul></div>
  <div class="card price-card" style="left:106px;top:44px;width:76px;height:100px"><svg class="ic" style="margin-top:6px;color:#555"><use href="#i-globe"/></svg><div class="nm">Gold Trip</div><div class="band bg-y"><s style="opacity:.6">$2666</s> $2199</div><ul><li>Best services</li><li>Trusted since 1990</li><li>Low prices</li><li>Free booking fee</li></ul></div>
  <div class="card price-card" style="left:190px;top:44px;width:76px;height:100px"><svg class="ic" style="margin-top:6px;color:#555"><use href="#i-sun"/></svg><div class="nm">VIP Trip</div><div class="band bg-b">$8728</div><ul><li>Best services</li><li>Trusted since 1990</li><li>Low prices</li><li>Free booking fee</li></ul></div>
  <div class="brand">KVLO</div>
</section>

<section class="slide grey" style="left:902px;top:178px">
  <div class="a title center" style="top:16px;font-size:10px">Check our rate &amp; packages</div>
  <div class="card price-card" style="left:10px;top:44px;width:63px;height:100px"><svg class="ic" style="margin-top:6px;color:#555"><use href="#i-plane"/></svg><div class="nm">Silver Trip</div><div class="band bg-b">$1920</div><ul><li>Best services</li><li>Trusted since 1990</li><li>Low prices</li><li>Free booking fee</li></ul></div>
  <div class="card price-card" style="left:79px;top:44px;width:63px;height:100px"><svg class="ic" style="margin-top:6px;color:#555"><use href="#i-globe"/></svg><div class="nm">Silver Trip</div><div class="band bg-y">$1920</div><ul><li>Best services</li><li>Trusted since 1990</li><li>Low prices</li><li>Free booking fee</li></ul></div>
  <div class="card price-card" style="left:148px;top:44px;width:63px;height:100px"><svg class="ic" style="margin-top:6px;color:#555"><use href="#i-sun"/></svg><div class="nm">Silver Trip</div><div class="band bg-g">$1920</div><ul><li>Best services</li><li>Trusted since 1990</li><li>Low prices</li><li>Free booking fee</li></ul></div>
  <div class="card price-card" style="left:217px;top:44px;width:63px;height:100px"><svg class="ic" style="margin-top:6px;color:#555"><use href="#i-pin"/></svg><div class="nm">Silver Trip</div><div class="band bg-k">$1920</div><ul><li>Best services</li><li>Trusted since 1990</li><li>Low prices</li><li>Free booking fee</li></ul></div>
  <div class="brand">KVLO</div>
</section>

<!-- Row 3 -->
<section class="slide" style="left:11px;top:349px">
  <div class="photo forest" style="inset:0" role="img" aria-label="Hiker crossing a wooden bridge through a dark forest"></div>
  <div class="a" style="left:30px;top:36px;font-size:3.6px;color:var(--yellow)">KVLO EXTRA</div>
  <div class="a title white" style="left:30px;top:45px;font-size:10px">Exclusive Travel<br>Rewards For<br>You</div>
  <div class="card price-card" style="left:188px;top:28px;width:66px;height:62px"><svg class="ic b" style="margin-top:5px"><use href="#i-car"/></svg><div class="nm" style="font-size:6px">14 days Trip!</div><div class="band bg-y">only $2827</div><div class="tx" style="padding:3px">Bali, Sulawesi, Papua</div></div>
  <div class="a tx w" style="left:30px;top:128px;width:228px">Trip planning today can be challenging. With hundreds of websites, discount sites and hotels it can seem overwhelming. This network is the exclusive service, offering premium travel opportunities at discount rates. Book everything in one place.</div>
</section>

<section class="slide" style="left:308px;top:349px;background:var(--dark)">
  <div class="photo sea" style="left:0;top:0;right:0;height:95px" role="img" aria-label="Overwater villas on a turquoise lagoon"></div>
  <div class="a center" style="top:22px;font-size:3.6px;color:var(--yellow)">KVLO EXTRA</div>
  <div class="a title white center" style="top:31px;font-size:9px">Exclusive Travel<br>Rewards For You</div>
  <div class="card price-card" style="left:44px;top:73px;width:64px;height:60px"><svg class="ic b" style="margin-top:4px"><use href="#i-car"/></svg><div class="nm">14 days Trip!</div><div class="band bg-y">only $2827</div><div class="tx" style="padding:3px">Bali, Sulawesi, Papua</div></div>
  <div class="card price-card" style="left:112px;top:73px;width:64px;height:60px"><svg class="ic b" style="margin-top:4px"><use href="#i-plane"/></svg><div class="nm">14 days Trip!</div><div class="band bg-g">only $2827</div><div class="tx" style="padding:3px">Bali, Sulawesi, Papua</div></div>
  <div class="card price-card" style="left:180px;top:73px;width:64px;height:60px"><svg class="ic b" style="margin-top:4px"><use href="#i-sail"/></svg><div class="nm">14 days Trip!</div><div class="band bg-b">only $2827</div><div class="tx" style="padding:3px">Bali, Sulawesi, Papua</div></div>
</section>

<section class="slide" style="left:605px;top:349px">
  <div class="a title center" style="top:16px;font-weight:400">Begin Your Adventure</div>
  <div class="photo sea" style="left:9px;top:32px;width:134px;height:61px" role="img" aria-label="Boats on a blue bay"><div class="tile-lab">Java</div></div>
  <div class="photo beach" style="left:145px;top:32px;width:134px;height:61px" role="img" aria-label="Beach umbrellas by a pool"><div class="tile-lab">Sumatra</div></div>
  <div class="photo beach" style="left:9px;top:95px;width:134px;height:61px" role="img" aria-label="Lounge chair at sunset"><div class="tile-lab">Seribu</div></div>
  <div class="photo sea" style="left:145px;top:95px;width:134px;height:61px" role="img" aria-label="Clear tropical water"><div class="tile-lab">Borneo</div></div>
</section>

<section class="slide" style="left:902px;top:349px">
  <div class="a title center" style="top:16px">The Sea is Calling</div>
  <div class="a" style="left:0;top:38px;width:150px;height:74px;background:#3a3a3a"></div>
  <div class="photo sea" style="left:142px;top:38px;right:0;height:74px" role="img" aria-label="Speedboat on a turquoise sea"></div>
  <div class="a" style="left:18px;top:50px;font-size:4.5px;color:#ccc">BALI • LOMBOK</div>
  <div class="a tx w" style="left:18px;top:60px;width:110px">This network is the exclusive service, offering premium travel opportunities at discount rates.</div>
  <div class="a" style="left:18px;top:82px;font-size:3px;color:var(--yellow)">→ 10 DESTINATIONS IN 3 DAYS</div>
  <div class="a tx" style="left:30px;top:122px;width:230px">Trip planning today can be challenging. With hundreds of websites, discount sites and hotels it can seem overwhelming.</div>
  <div class="brand">KVLO</div>
</section>

<!-- Row 4 -->
<section class="slide" style="left:11px;top:519px">
  <div class="a title center" style="top:14px">KVLO <b>EXTRA</b></div>
  <div class="a rule" style="left:134px;top:41px"></div>
  <div class="card" style="left:22px;top:58px;width:62px;height:82px;text-align:center">
    <div class="lab b" style="margin-top:5px">STAY</div>
    <div class="photo sea" style="position:relative;margin:4px auto;width:34px;height:34px;border-radius:50%" role="img" aria-label="Traveller portrait by the sea"></div>
    <div style="margin:6px auto 0;width:44px;border:.5px solid #999;font-size:3.4px;padding:1px">$12.99/night</div>
  </div>
  <div class="a tx" style="left:90px;top:66px;width:50px;line-height:2">→ FRIENDLY PLACE<br>→ FAMILY PACKAGE<br>→ FREE SERVICE<br>→ GET MORE DEALS</div>
  <div class="card" style="left:146px;top:58px;width:62px;height:82px;text-align:center">
    <div class="lab b" style="margin-top:5px">FRIENDS</div>
    <div class="photo beach" style="position:relative;margin:4px auto;width:34px;height:34px;border-radius:50%" role="img" aria-label="Group of friends on holiday"></div>
    <div style="margin:6px auto 0;width:44px;border:.5px solid #999;font-size:3.4px;padding:1px">$12.99/night</div>
  </div>
  <div class="a tx" style="left:214px;top:66px;width:52px;line-height:2">→ GROUP TRIP<br>→ 10 DESTINATIONS<br>→ MARATHON ROUTE<br>→ CHEAP RENT</div>
  <div class="brand">KVLO</div>
</section>

<section class="slide" style="left:308px;top:519px">
  <div class="a title center" style="top:14px">KVLO <b>EXTRA</b></div>
  <div class="a rule" style="left:134px;top:41px"></div>
  <div class="a tx center" style="top:56px;padding:0 34px">Trip planning today can be challenging. With hundreds of websites, discount sites and hotels it can seem overwhelming. This network offers premium travel at discount rates.</div>
  <div class="a center" style="top:86px;display:flex;justify-content:space-around;padding:0 26px;text-align:center">
    <div style="width:66px"><svg class="ic y"><use href="#i-plane"/></svg><div class="lab">STAY</div><div class="tx">Rent or bid on weekly stay vacations at your price.</div></div>
    <div style="width:66px"><svg class="ic g"><use href="#i-mount"/></svg><div class="lab">LOGISTICS</div><div class="tx">Rent or bid on weekly stay vacations at your price.</div></div>
    <div style="width:66px"><svg class="ic b"><use href="#i-sail"/></svg><div class="lab">SAIL &amp; FISHING</div><div class="tx">Rent or bid on weekly stay vacations at your price.</div></div>
  </div>
  <div class="brand">KVLO</div>
</section>

<section class="slide" style="left:605px;top:519px">
  <div class="a title center" style="top:14px">KVLO <b>EXTRA</b></div>
  <div class="a rule" style="left:134px;top:41px"></div>
  <div class="a center" style="top:50px;display:flex;justify-content:space-around;padding:0 20px;text-align:center">
    <div style="width:70px"><svg class="ic g"><use href="#i-plane"/></svg><div class="lab">REWARD CREDITS</div><div class="tx">Rent or bid on weekly stay vacations at your price.</div></div>
    <div style="width:70px"><svg class="ic g"><use href="#i-mount"/></svg><div class="lab">400,000+ HOTELS</div><div class="tx">Rent or bid on weekly stay vacations at your price.</div></div>
    <div style="width:70px"><svg class="ic g"><use href="#i-sail"/></svg><div class="lab">MARKETPLACE</div><div class="tx">Rent or bid on weekly stay vacations at your price.</div></div>
  </div>
  <div class="a center" style="top:100px;display:flex;justify-content:space-around;padding:0 20px;text-align:center">
    <div style="width:70px"><svg class="ic y"><use href="#i-sun"/></svg><div class="lab">BOOMERANG</div><div class="tx">Rent or bid on weekly stay vacations at your price.</div></div>
    <div style="width:70px"><svg class="ic y"><use href="#i-sail"/></svg><div class="lab">PRICE GUARANTEE</div><div class="tx">Rent or bid on weekly stay vacations at your price.</div></div>
    <div style="width:70px"><svg class="ic y"><use href="#i-car"/></svg><div class="lab">LIVE CHAT</div><div class="tx">Rent or bid on weekly stay vacations at your price.</div></div>
  </div>
  <div class="brand">KVLO</div>
</section>

<section class="slide" style="left:902px;top:519px">
  <div class="photo sea" style="left:0;top:0;right:0;height:100px;clip-path:polygon(0 0,100% 0,100% 85%,0 100%)" role="img" aria-label="Overwater bungalow on a calm lagoon"></div>
  <div class="a" style="left:28px;top:10px;font-size:3.6px">KVLO <b>EXTRA</b></div>
  <div class="a title" style="left:28px;top:20px;font-weight:400">Exclusive Travel<br>Rewards For<br>You</div>
  <div class="a rule" style="left:28px;top:56px;background:var(--yellow)"></div>
  <div class="a stars" style="left:30px;top:110px">★★★★★</div>
  <div class="btn bg-g" style="left:30px;top:124px">Scandinavia Trip</div>
  <div class="a tx" style="left:106px;top:114px;width:164px;text-align:justify">Trip planning today can be challenging. With hundreds of websites, discount sites and hotels it can seem overwhelming. This network offers premium travel opportunities at discount rates.</div>
  <div class="brand">KVLO</div>
</section>

<!-- Row 5 -->
<section class="slide" style="left:11px;top:690px">
  <div class="photo beach" style="left:16px;top:16px;width:140px;height:130px" role="img" aria-label="Lounge chair facing a calm sunset sea"></div>
  <div class="card" style="left:153px;top:31px;width:99px;height:102px;padding:10px 8px">
    <div style="font-size:10px;font-weight:600">Thailand</div>
    <div class="tx" style="color:var(--yellow)">• BRUNEI / INDONESIA</div>
    <div class="band bg-y" style="margin:5px 0">10 DESTINATIONS IN 3 DAYS</div>
    <div style="display:flex;justify-content:space-around"><svg class="ic g"><use href="#i-hotel"/></svg><svg class="ic g"><use href="#i-plane"/></svg><svg class="ic g"><use href="#i-pin"/></svg></div>
    <div class="tx" style="margin-top:4px">This network is the exclusive service, offering premium travel at discount rates.</div>
  </div>
  <div class="brand">KVLO</div>
</section>

<section class="slide" style="left:308px;top:690px">
  <div class="photo beach" style="left:116px;top:16px;width:140px;height:130px" role="img" aria-label="Umbrellas and loungers at a pool edge"></div>
  <div class="card" style="left:32px;top:31px;width:99px;height:102px;padding:10px 8px">
    <div style="font-size:10px;font-weight:600">Indonesia</div>
    <div class="tx" style="color:var(--yellow)">• FIJI / PAPUA NG</div>
    <div class="band bg-y" style="margin:5px 0">10 DESTINATIONS IN 3 DAYS</div>
    <div style="display:flex;justify-content:space-around;color:var(--dark)"><svg class="ic"><use href="#i-hotel"/></svg><svg class="ic"><use href="#i-plane"/></svg><svg class="ic"><use href="#i-pin"/></svg></div>
    <div class="tx" style="margin-top:4px">This network is the exclusive service, offering premium travel at discount rates.</div>
  </div>
  <div class="brand" style="left:6px;right:auto">KVLO</div>
</section>

<section class="slide" style="left:605px;top:690px">
  <div class="photo meadow" style="left:0;top:0;right:0;height:70px;opacity:.8" role="img" aria-label="Hiker looking over green hills"></div>
  <div class="a" style="left:18px;top:12px;font-size:9px;color:#fff;font-weight:300">Discover</div>
  <div class="card" style="left:44px;top:34px;width:64px;height:100px;text-align:center">
    <div class="photo beach" style="position:relative;height:40px" role="img" aria-label="Resort pool"></div>
    <div class="tx" style="color:var(--yellow);font-size:2.8px;margin-top:2px">COMPLETE PACK</div><div class="lab">THAILAND</div>
    <div class="tx">Book your flight, hotel and more all in one place.</div>
    <div class="tx" style="color:var(--yellow);margin-top:3px">3 days, 2 night · 5 stars</div></div>
  <div class="card" style="left:112px;top:30px;width:64px;height:108px;text-align:center">
    <div class="photo room" style="position:relative;height:44px" role="img" aria-label="Hotel bedroom"></div>
    <div class="tx" style="color:var(--yellow);font-size:2.8px;margin-top:2px">COMPLETE PACK</div><div class="lab">BALI • LOMBOK</div>
    <div class="tx">Book your flight, hotel and more all in one place.</div>
    <div class="tx" style="color:var(--yellow);margin-top:3px">3 days, 2 night · 5 stars</div></div>
  <div class="card" style="left:180px;top:34px;width:64px;height:100px;text-align:center">
    <div class="photo sea" style="position:relative;height:40px" role="img" aria-label="Island lagoon"></div>
    <div class="tx" style="color:var(--yellow);font-size:2.8px;margin-top:2px">COMPLETE PACK</div><div class="lab">FIJI ISLANDS</div>
    <div class="tx">Book your flight, hotel and more all in one place.</div>
    <div class="tx" style="color:var(--yellow);margin-top:3px">3 days, 2 night · 5 stars</div></div>
  <div class="brand" style="left:6px;right:auto">KVLO</div>
</section>

<section class="slide" style="left:902px;top:690px">
  <div class="photo forest" style="inset:0;background:linear-gradient(160deg,#2d5a2a,#6f9a48 60%,#e9ece4 60%)" role="img" aria-label="Waterfall in a tropical jungle"></div>
  <div class="a title white" style="left:22px;top:30px;font-size:9.5px">Exclusive Travel<br>Rewards For You</div>
  <div class="a tx" style="left:22px;top:88px;width:120px;text-align:justify;color:#666">Trip planning today can be challenging. With hundreds of websites, discount sites and hotels it can seem overwhelming. This network offers premium travel at discount rates.</div>
  <div class="card" style="left:176px;top:26px;width:72px;height:104px;text-align:center">
    <div class="photo room" style="position:relative;height:46px" role="img" aria-label="Hotel bedroom"></div>
    <div class="tx" style="color:var(--yellow);font-size:2.8px;margin-top:2px">COMPLETE PACK</div><div class="lab">BALI • LOMBOK</div>
    <div class="tx">Book your flight, hotel and more all in one place.</div>
    <div class="tx" style="color:var(--yellow);margin-top:3px">3 days, 2 night · 5 stars</div></div>
  <div class="brand" style="left:6px;right:auto">KVLO</div>
</section>

<!-- Row 6 -->
<section class="slide" style="left:11px;top:860px">
  <div class="photo room" style="left:17px;top:17px;width:100px;height:129px" role="img" aria-label="Hotel bedroom with white linen"></div>
  <div class="a title" style="left:138px;top:18px;font-size:9px">Exclusive Travel<br>Rewards For You</div>
  <div class="strip" style="left:138px;top:54px;width:124px"><div class="bg-y"><svg class="ic"><use href="#i-plane"/></svg>BUDGET FLIGHT</div><div><svg class="ic b"><use href="#i-people"/></svg>GROUP TRIP</div><div><svg class="ic b"><use href="#i-hotel"/></svg>NEAR HOTELS</div></div>
  <div class="a tx" style="left:138px;top:80px;width:124px;text-align:justify">Trip planning today can be challenging. With hundreds of websites, discount sites and hotels it can seem overwhelming. This network offers premium travel at discount rates.</div>
  <div class="btn bg-g" style="left:138px;top:118px;width:88px">20% DISCOUNT DURING SUMMER</div>
  <div class="brand">KVLO</div>
</section>

<section class="slide" style="left:308px;top:860px">
  <div class="photo meadow" style="inset:0" role="img" aria-label="Backpacker overlooking a green valley"></div>
  <div class="a title white" style="left:16px;top:12px;font-size:9px;font-weight:400">Budget Trip, Save More<br>Money in Group.</div>
  <div class="strip" style="left:16px;top:48px;width:124px"><div class="bg-b"><svg class="ic"><use href="#i-plane"/></svg>BUDGET FLIGHT</div><div><svg class="ic b"><use href="#i-people"/></svg>GROUP TRIP</div><div><svg class="ic b"><use href="#i-hotel"/></svg>NEAR HOTELS</div></div>
  <div class="a tx" style="left:16px;top:72px;width:124px;color:#333;text-align:justify">Trip planning today can be challenging. With hundreds of websites, discount sites and hotels it can seem overwhelming. This network offers premium travel at discount rates.</div>
  <div class="btn bg-y" style="left:16px;top:118px">20% DISCOUNT DURING SUMMER</div>
</section>

<section class="slide" style="left:605px;top:860px">
  <div class="photo sea" style="left:0;top:0;right:0;height:95px" role="img" aria-label="Overwater villas beside palm trees"></div>
  <div class="a title white center" style="top:24px;font-size:9px">Budget Trip, Save More<br>Money in Group.</div>
  <div class="strip" style="left:42px;top:62px;width:204px"><div class="bg-g"><svg class="ic"><use href="#i-plane"/></svg>BUDGET FLIGHT</div><div><svg class="ic y"><use href="#i-people"/></svg>GROUP TRIP</div><div><svg class="ic b"><use href="#i-hotel"/></svg>NEAR HOTELS</div><div><svg class="ic g"><use href="#i-pin"/></svg>PRO GUIDE</div><div><svg class="ic" style="color:#666"><use href="#i-sail"/></svg>SAIL &amp; FISHING</div></div>
  <div class="a tx center" style="top:104px;padding:0 26px">Trip planning today can be challenging. With hundreds of websites, discount sites and hotels it can seem overwhelming. This network offers premium travel opportunities at discount rates. Book your flight, hotel and more in one place.</div>
  <div class="brand">KVLO</div>
</section>

<section class="slide grey" style="left:902px;top:860px">
  <div class="a title center" style="top:14px;font-weight:400">Event Calendar</div>
  <div class="a" style="left:30px;top:40px;width:72px;height:86px;background:#e2e2e2;padding:6px">
    <div class="tx"><svg class="ic b" style="width:5px;height:5px"><use href="#i-cal"/></svg> DECEMBER 2020</div>
    <div style="font-size:7px;margin:8px 0 3px">Mountain<br>Survival</div>
    <div class="tx">This network is the exclusive service offering premium travel at discount rates.</div></div>
  <div class="card" style="left:98px;top:28px;width:92px;height:116px;text-align:center">
    <div class="photo beach" style="position:relative;height:46px" role="img" aria-label="Resort pool with umbrellas"></div>
    <div class="band bg-y" style="margin:0 22px;font-size:2.8px">BOOKING FREE</div>
    <div class="tx" style="margin-top:3px">SEPTEMBER 2019</div>
    <div style="font-size:7px;margin:3px 0">Wild West Wave</div>
    <div class="tx" style="padding:0 8px">This network is the exclusive service offering premium travel at discount rates.</div></div>
  <div class="a" style="left:186px;top:40px;width:74px;height:86px;background:#dff0d2;padding:6px 8px">
    <div class="tx"><svg class="ic g" style="width:5px;height:5px"><use href="#i-cal"/></svg> OCTOBER 2019</div>
    <div style="font-size:7px;margin:8px 0 3px">Backpacker<br>Badgers</div>
    <div class="tx">This network is the exclusive service offering premium travel.</div>
    <div class="tx" style="color:var(--yellow);margin-top:3px">3 days, 2 night · 5 stars</div></div>
</section>

<!-- Row 7 -->
<section class="slide grey" style="left:11px;top:1030px">
  <div class="a title center" style="top:12px;font-weight:400">Event Calendar</div>
  <div class="card" style="left:14px;top:30px;width:85px;height:132px;text-align:center">
    <div class="photo sea" style="position:relative;height:56px" role="img" aria-label="Couple with a map by the sea"></div>
    <div class="band bg-y" style="margin:0 20px;font-size:2.8px">BOOKING FREE</div>
    <div class="tx" style="margin-top:3px">SEPTEMBER 2019</div><div style="font-size:7px;margin:3px 0">Wild West Wave</div>
    <div class="tx" style="padding:0 6px">This network is the exclusive service offering premium travel at discount rates.</div></div>
  <div class="card" style="left:102px;top:30px;width:85px;height:132px;text-align:center">
    <div class="photo forest" style="position:relative;height:56px" role="img" aria-label="Hiker on a forest bridge"></div>
    <div class="band bg-y" style="margin:0 20px;font-size:2.8px">BOOKING FREE</div>
    <div class="tx" style="margin-top:3px">SEPTEMBER 2019</div><div style="font-size:7px;margin:3px 0">Top Peak</div>
    <div class="tx" style="padding:0 6px">This network is the exclusive service offering premium travel at discount rates.</div></div>
  <div class="card" style="left:190px;top:30px;width:85px;height:132px;text-align:center">
    <div class="photo meadow" style="position:relative;height:56px" role="img" aria-label="Backpacker on a cliff"></div>
    <div class="band bg-y" style="margin:0 20px;font-size:2.8px">BOOKING FREE</div>
    <div class="tx" style="margin-top:3px">SEPTEMBER 2019</div><div style="font-size:7px;margin:3px 0">Cliff Camp</div>
    <div class="tx" style="padding:0 6px">This network is the exclusive service offering premium travel at discount rates.</div></div>
</section>

<section class="slide grey" style="left:308px;top:1030px">
  <div class="a title center" style="top:12px;font-weight:400">Choose Your Best</div>
  <div class="card" style="left:16px;top:30px;width:128px;height:58px"><div class="photo sea" style="left:3px;top:3px;width:58px;height:52px" role="img" aria-label="Whitewashed seaside houses"></div><div class="a" style="left:66px;top:5px;font-size:7px;color:var(--yellow);font-weight:600">$35</div><div class="a tx" style="left:66px;top:16px;width:56px">Book your flight, hotel, excursions and more all in one place.</div><div class="a" style="left:66px;top:44px;display:flex;gap:4px"><svg class="ic y" style="width:5px;height:5px"><use href="#i-bed"/></svg><svg class="ic y" style="width:5px;height:5px"><use href="#i-wifi"/></svg></div></div>
  <div class="card" style="left:146px;top:30px;width:128px;height:58px"><div class="photo room" style="left:3px;top:3px;width:58px;height:52px" role="img" aria-label="City hotel building"></div><div class="a" style="left:66px;top:5px;font-size:7px;color:var(--yellow);font-weight:600">$35</div><div class="a tx" style="left:66px;top:16px;width:56px">Book your flight, hotel, excursions and more all in one place.</div><div class="a" style="left:66px;top:44px;display:flex;gap:4px"><svg class="ic y" style="width:5px;height:5px"><use href="#i-bed"/></svg><svg class="ic y" style="width:5px;height:5px"><use href="#i-wifi"/></svg></div></div>
  <div class="card" style="left:16px;top:92px;width:128px;height:58px"><div class="photo beach" style="left:3px;top:3px;width:58px;height:52px" role="img" aria-label="Tropical villa"></div><div class="a" style="left:66px;top:5px;font-size:7px;color:var(--yellow);font-weight:600">$35</div><div class="a tx" style="left:66px;top:16px;width:56px">Book your flight, hotel, excursions and more all in one place.</div><div class="a" style="left:66px;top:44px;display:flex;gap:4px"><svg class="ic y" style="width:5px;height:5px"><use href="#i-bed"/></svg><svg class="ic y" style="width:5px;height:5px"><use href="#i-wifi"/></svg></div></div>
  <div class="card" style="left:146px;top:92px;width:128px;height:58px"><div class="photo sea" style="left:3px;top:3px;width:58px;height:52px" role="img" aria-label="Resort pool with loungers"></div><div class="a" style="left:66px;top:5px;font-size:7px;color:var(--yellow);font-weight:600">$35</div><div class="a tx" style="left:66px;top:16px;width:56px">Book your flight, hotel, excursions and more all in one place.</div><div class="a" style="left:66px;top:44px;display:flex;gap:4px"><svg class="ic y" style="width:5px;height:5px"><use href="#i-bed"/></svg><svg class="ic y" style="width:5px;height:5px"><use href="#i-wifi"/></svg></div></div>
</section>

<section class="slide" style="left:605px;top:1030px">
  <div class="a" style="left:20px;top:10px;font-size:2.8px;color:var(--muted)">PACKAGE BASED ON ADVENTURE TYPE</div>
  <div class="a" style="left:20px;top:17px;font-size:9px">Choose Your Vacation</div>
  <div class="a" style="left:20px;top:44px;width:76px"><div class="lab b">BACKPACKER</div><div class="tx">This network is the exclusive service, offering premium travel at discount rates.</div></div>
  <div class="a" style="left:108px;top:44px;width:76px"><div class="lab b">CITY TOUR</div><div class="tx">This network is the exclusive service, offering premium travel at discount rates.</div></div>
  <div class="a" style="left:196px;top:44px;width:76px"><div class="lab b">SAIL &amp; DIVE</div><div class="tx">This network is the exclusive service, offering premium travel at discount rates.</div></div>
  <div class="a" style="left:20px;top:82px;width:76px"><div class="lab b">GROUP</div><div class="tx">This network is the exclusive service, offering premium travel at discount rates.</div></div>
  <div class="a" style="left:108px;top:82px;width:76px"><div class="lab b">HONEY MOON</div><div class="tx">This network is the exclusive service, offering premium travel at discount rates.</div></div>
  <div class="a" style="left:196px;top:82px;width:76px"><div class="lab b">EXTREME</div><div class="tx">This network is the exclusive service, offering premium travel at discount rates.</div></div>
  <div class="photo" style="left:0;right:0;top:126px;bottom:0;background:linear-gradient(90deg,#6fb9d8,#3d4a3a 30%,#cfd7de 55%,#7d6b4f 75%,#f0c88a)" role="img" aria-label="Strip of travel scenes: sea, forest, city and sunset"></div>
</section>

<section class="slide" style="left:902px;top:1030px">
  <div class="a bg-b" style="left:0;top:0;width:76px;height:162px"></div>
  <div class="a" style="left:0;top:14px;width:76px;text-align:center;color:#fff">
    <svg class="ic"><use href="#i-hotel"/></svg><div style="font-size:2.8px;font-weight:700;margin-bottom:12px">FREE DELICIOUS<br>BREAKFAST</div>
    <svg class="ic"><use href="#i-bed"/></svg><div style="font-size:2.8px;font-weight:700;margin-bottom:12px">FREE 1 EXTRA<br>BED</div>
    <svg class="ic"><use href="#i-pin"/></svg><div style="font-size:2.8px;font-weight:700;margin-bottom:12px">PET FRIENDLY</div>
    <svg class="ic"><use href="#i-people"/></svg><div style="font-size:2.8px;font-weight:700">FAMILY GAME<br>AND PLAY</div>
  </div>
  <div class="photo" style="left:76px;top:0;right:0;bottom:0;background:linear-gradient(160deg,#bcdcf0,#d9c6a4 55%,#8e7c63)" role="img" aria-label="Smiling couple with a city map in front of a historic building"></div>
</section>
</body>
</html>
```